Business Card for my building company

I would like the card to make a statement, so as soon as you see the card you think "wow nice card' and then read the details on the card its self. Also i would like to be able to put in the detail for the MUST HAVES so please Crete a box that i can alter depending on who in my business needs the cards. Thank you

Target Market(s)

Any one looking to build a house/ townhouse or duplex

Industry/Entity Type

Home Builder

Contact Information for Business Card

I would like the card to have the logo on the card and the must haves

Font styles to use
Sans Serif

Requirements
Must have
• Name
• Phone Number
• Email Address
• Website
• Licence Number
• Abn

```html
<!DOCTYPE html>
<html lang="en">
<head>
<meta charset="utf-8">
<title>Northline Builders – Business Card</title>
<link href="https://fonts.googleapis.com/css2?family=Open+Sans:wght@400;600;700&display=swap" rel="stylesheet">
<style>
  :root {
    --bg: #2a2622;
    --card-top: #1c1c1c;
    --card-bottom: #050505;
    --gold: #c9a84c;
    --gold-dark: #8f7431;
    --white: #f4f4f4;
    --muted: #d8d8d8;
  }
  html, body {
    margin: 0;
    width: 1200px;
    height: 1022px;
    overflow: hidden;
    background: var(--bg);
    font-family: "Open Sans", Arial, sans-serif;
  }
  .stage {
    width: 1200px;
    height: 1022px;
    display: flex;
    align-items: center;
    justify-content: center;
  }
  .card {
    position: relative;
    width: 1000px;
    height: 580px;
    border-radius: 26px;
    background: linear-gradient(160deg, var(--card-top) 0%, #0d0d0d 45%, var(--card-bottom) 100%);
    overflow: hidden;
    color: var(--white);
  }
  .brand {
    position: absolute;
    left: 60px;
    top: 150px;
    display: flex;
    align-items: center;
    gap: 18px;
  }
  .brand-square {
    width: 70px;
    height: 70px;
    background: var(--gold);
  }
  .brand-name {
    font-weight: 700;
    font-size: 44px;
    line-height: 1.05;
    color: var(--gold);
    text-transform: uppercase;
    letter-spacing: 1px;
  }
  .licence {
    position: absolute;
    left: 60px;
    top: 262px;
    font-size: 22px;
    color: var(--white);
  }
  .licence .label { color: var(--gold); }
  .address {
    position: absolute;
    left: 60px;
    top: 318px;
    font-size: 22px;
    color: var(--muted);
  }
  .divider {
    position: absolute;
    left: 60px;
    right: 70px;
    top: 360px;
    height: 3px;
    background: var(--gold);
  }
  .contact-list {
    position: absolute;
    left: 60px;
    top: 378px;
    margin: 0;
    padding: 0;
    list-style: none;
    font-size: 22px;
    color: var(--white);
  }
  .contact-list li {
    display: flex;
    align-items: center;
    gap: 14px;
    height: 38px;
  }
  .contact-list svg { width: 18px; height: 18px; fill: var(--gold); flex: none; }
  .person {
    position: absolute;
    right: 110px;
    top: 300px;
    text-align: right;
  }
  .person-name {
    font-weight: 700;
    font-size: 44px;
    line-height: 1;
    letter-spacing: 1px;
    text-transform: uppercase;
  }
  .person-role {
    position: absolute;
    right: 110px;
    top: 372px;
    font-size: 20px;
    letter-spacing: 1px;
    color: var(--gold);
    text-transform: uppercase;
  }
  .abn {
    position: absolute;
    right: 110px;
    top: 470px;
    font-size: 20px;
    color: var(--muted);
  }
  .edge-tab {
    position: absolute;
    right: 0;
    top: 300px;
    width: 42px;
    height: 100px;
    display: flex;
    gap: 6px;
  }
  .edge-tab span { flex: 1; background: var(--gold); }
  .edge-tab span:first-child { background: var(--gold-dark); }
</style>
</head>
<body>
<main class="stage">
  <article class="card">
    <div class="brand">
      <div class="brand-square"></div>
      <div class="brand-name">Northline<br>Builders</div>
    </div>

    <p class="licence" style="margin:0"><span class="label">#LIC :</span> 2046517</p>
    <p class="address" style="margin:0">Fairview QLD 4100</p>

    <div class="divider"></div>

    <ul class="contact-list">
      <li>
        <svg viewBox="0 0 24 24" aria-hidden="true"><path d="M6.6 10.8a15.1 15.1 0 0 0 6.6 6.6l2.2-2.2c.3-.3.7-.4 1-.2 1.1.4 2.3.6 3.6.6.6 0 1 .4 1 1V20c0 .6-.4 1-1 1C10.6 21 3 13.4 3 4c0-.6.4-1 1-1h3.5c.6 0 1 .4 1 1 0 1.3.2 2.5.6 3.6.1.3 0 .7-.2 1z"/></svg>
        0400 318 642
      </li>
      <li>
        <svg viewBox="0 0 24 24" aria-hidden="true"><path d="M3 5h18v14H3zm2 2v.5l7 4.5 7-4.5V7zm0 2.9V17h14V9.9l-7 4.5z"/></svg>
        info@danielhartmail.com
      </li>
      <li>
        <svg viewBox="0 0 24 24" aria-hidden="true"><path d="M12 2a10 10 0 1 0 0 20 10 10 0 0 0 0-20zm6.9 6h-2.9a15.6 15.6 0 0 0-1.4-3.6A8 8 0 0 1 18.9 8zM12 4c.8 1.2 1.5 2.5 1.9 4h-3.8c.4-1.5 1.1-2.8 1.9-4zM4.3 14a8 8 0 0 1 0-4h3.4a16.5 16.5 0 0 0 0 4zm.8 2h2.9c.3 1.3.8 2.5 1.4 3.6A8 8 0 0 1 5.1 16zM8 8H5.1a8 8 0 0 1 4.3-3.6C8.8 5.5 8.3 6.7 8 8zm4 12c-.8-1.2-1.5-2.5-1.9-4h3.8c-.4 1.5-1.1 2.8-1.9 4zm2.3-6H9.7a14.7 14.7 0 0 1 0-4h4.6a14.7 14.7 0 0 1 0 4zm.3 5.6c.6-1.1 1.1-2.3 1.4-3.6h2.9a8 8 0 0 1-4.3 3.6zM16.3 14a16.5 16.5 0 0 0 0-4h3.4a8 8 0 0 1 0 4z"/></svg>
        www.northlinebuilders.com
      </li>
    </ul>

    <div class="person"><div class="person-name">Daniel Hart</div></div>
    <div class="person-role">Director</div>
    <p class="abn" style="margin:0">ABN : 48 210 774 136</p>

    <div class="edge-tab"><span></span><span></span></div>
  </article>
</main>
</body>
</html>
```